Electrician Letterhead Design QVL

We need some letterhead for our bills and other papers.
Customer address is on the right side (Swiss format)
A4 format

Design should also be applicable on Cards

Target Market(s)

Private Customers, Small Business

Industry/Entity Type

Electrician

Other font styles liked:
• incised 901

Colors
00AB8E
00BBA5
67D7C9
C6EFE9
E9F9F6

```html
<!DOCTYPE html>
<html lang="de">
<head>
<meta charset="utf-8">
<title>QVL Letterhead</title>
<link rel="stylesheet" href="https://fonts.googleapis.com/css2?family=Poppins:wght@400;500;700;800&display=swap">
<style>
  :root {
    --backdrop: #55b9a9;
    --paper: #ffffff;
    --brand-teal: #3f9886;
    --brand-teal-light: #67d7c9;
    --ink: #111111;
    --rule: #e6e9e8;
  }
  * { margin: 0; padding: 0; box-sizing: border-box; }
  html, body {
    width: 1200px;
    height: 1192px;
    overflow: hidden;
    background: var(--backdrop);
    font-family: "Poppins", sans-serif;
  }
  .canvas {
    position: relative;
    width: 1200px;
    height: 1192px;
  }
  .letterhead {
    position: absolute;
    left: 218px;
    top: 56px;
    width: 764px;
    height: 1080px;
    background: var(--paper);
    overflow: hidden;
    box-shadow: 0 24px 60px rgba(0, 40, 32, 0.28);
  }
  .brand {
    position: absolute;
    left: 44px;
    top: 44px;
    display: flex;
    flex-direction: column;
    gap: 4px;
  }
  .brand-row {
    display: flex;
    align-items: center;
    gap: 12px;
  }
  .brand-name {
    font-weight: 800;
    font-size: 64px;
    line-height: 1;
    letter-spacing: 1px;
    color: var(--brand-teal);
  }
  .brand-mark {
    width: 18px;
    height: 18px;
    background: var(--brand-teal);
  }
  .brand-legal {
    font-weight: 700;
    font-size: 10.5px;
    color: var(--ink);
    letter-spacing: 0.2px;
  }
  .contact {
    position: absolute;
    right: 44px;
    top: 50px;
    list-style: none;
    display: flex;
    flex-direction: column;
    gap: 6px;
  }
  .contact-item {
    display: flex;
    align-items: center;
    justify-content: flex-end;
    gap: 14px;
    font-size: 12.5px;
    font-weight: 500;
    color: var(--ink);
  }
  .contact-icon {
    width: 11px;
    height: 11px;
    fill: var(--brand-teal);
  }
  .header-rule {
    position: absolute;
    left: 44px;
    right: 44px;
    top: 168px;
    height: 1px;
    background: var(--rule);
  }
  .footer-band {
    position: absolute;
    left: 0;
    bottom: 0;
    width: 764px;
    height: 200px;
  }
</style>
</head>
<body>
<div class="canvas">
  <section class="letterhead">
    <header>
      <div class="brand">
        <div class="brand-row">
          <span class="brand-name">QVL</span>
          <span class="brand-mark"></span>
        </div>
        <span class="brand-legal">Elektrotechnik Quovalen GmbH</span>
      </div>
      <ul class="contact">
        <li class="contact-item">Phone goes here
          <svg class="contact-icon" viewBox="0 0 24 24"><path d="M6.6 10.8a15.5 15.5 0 0 0 6.6 6.6l2.2-2.2a1 1 0 0 1 1-.25 11.4 11.4 0 0 0 3.6.57 1 1 0 0 1 1 1V20a1 1 0 0 1-1 1A17 17 0 0 1 3 4a1 1 0 0 1 1-1h3.5a1 1 0 0 1 1 1c0 1.25.2 2.45.57 3.57a1 1 0 0 1-.25 1z"/></svg>
        </li>
        <li class="contact-item">Email goes here
          <svg class="contact-icon" viewBox="0 0 24 24"><path d="M2 5h20v14H2z M4 7v.4l8 5 8-5V7l-8 5z" fill-rule="evenodd"/></svg>
        </li>
        <li class="contact-item">Website goes here
          <svg class="contact-icon" viewBox="0 0 24 24"><path d="M5 2l14 10-6 1.5 3.5 7-2.5 1.2-3.5-7L5 19z"/></svg>
        </li>
        <li class="contact-item">Adress goes here
          <svg class="contact-icon" viewBox="0 0 24 24"><path d="M12 2a7 7 0 0 0-7 7c0 5 7 13 7 13s7-8 7-13a7 7 0 0 0-7-7zm0 9.5a2.5 2.5 0 1 1 0-5 2.5 2.5 0 0 1 0 5z"/></svg>
        </li>
      </ul>
    </header>
    <div class="header-rule"></div>

    <svg class="footer-band" viewBox="0 0 764 200" preserveAspectRatio="none" aria-hidden="true">
      <path fill="var(--brand-teal-light)" d="M0,150 C220,120 480,60 764,40 L764,200 L0,200 Z"/>
      <path fill="var(--brand-teal)" d="M0,175 C260,150 520,100 764,90 L764,200 L0,200 Z"/>
      <path fill="none" stroke="var(--ink)" stroke-width="2" d="M0,140 C220,110 480,50 764,30"/>
    </svg>
  </section>
</div>
</body>
</html>
```